Tolvane - online store for farm produce

Online store selling fresh produce (vegetables, fruits, dairy products, meat, ...) from various farmers. Every farm has its own shopping window - order page - just like a really simple web store.

Please check the attached design brief and mock-ups for further details.

Target Market(s)

People looking for fresh vegetables, fruit, meat, ... delivered from farms

Industry/Entity Type

Farming

Coding

Coded - Design and coding required

Number of Pages Required

5+ page

Font styles to use
Sans Serif

Requirements
Must have
• Custom design. Good UX/UI design, very functional.
Responsive using bootstrap 12 point grid system

```html
<!DOCTYPE html>
<html lang="en">
<head>
<meta charset="utf-8">
<title>Tolvane – Product Search</title>
<link rel="stylesheet" href="https://fonts.googleapis.com/css2?family=Poppins:wght@300;400;500;600;700&display=swap">
<style>
:root{
  --green:#7ab80e;
  --green-dark:#6aa206;
  --hero:#abe9b0;
  --ink:#1c2839;
  --text:#333c48;
  --muted:#6b7380;
  --star:#f5b800;
  --orange:#f08a24;
  --chip:#eef1f4;
  --footer:#f1f4f8;
  --line:#e4e7eb;
  --white:#fff;
}
*{box-sizing:border-box;margin:0;padding:0}
html,body{width:1200px;height:2245px;overflow:hidden}
body{position:relative;background:var(--white);font-family:"Poppins",sans-serif;color:var(--text)}
.abs{position:absolute}
a{color:inherit;text-decoration:none}

/* header */
.site-header{left:0;top:0;width:1200px;height:89px}
.brand{left:81px;top:27px;font-size:25px;font-weight:700;color:var(--ink);letter-spacing:.5px}
.main-nav{left:422px;top:33px;display:flex;gap:48px;font-size:15px;font-weight:500;color:var(--ink)}
.btn-login{left:940px;top:23px;width:94px;height:40px;border-radius:20px;background:var(--green);color:#fff;font-size:13.5px;font-weight:500;display:flex;align-items:center;justify-content:center;gap:4px}
.link-logout{left:1045px;top:33px;font-size:13.5px;font-weight:500;color:var(--ink)}

/* hero */
.hero{left:0;top:89px;width:1200px;height:320px;background:var(--hero);overflow:hidden}
.hero h1{position:absolute;left:86px;top:112px;font-size:52px;font-weight:600;color:#fff;letter-spacing:.5px}
.crumbs{position:absolute;left:88px;top:178px;font-size:16.5px;font-weight:600;color:#fff}
.hero-leaf{left:0;top:240px;width:95px;height:80px;border-radius:0 60px 0 0;background:linear-gradient(135deg,#3d6b2b,#1f3d18)}
.hero-basket{left:612px;top:40px;width:540px;height:280px;border-radius:240px 240px 0 0;background:radial-gradient(ellipse at 50% 60%,#c8783a 0%,#b65a2a 30%,#6ea33a 60%,rgba(171,233,176,0) 78%)}

/* search */
.search-bar{left:197px;top:487px;width:788px;height:70px;border-radius:35px;background:#fff;box-shadow:0 6px 20px rgba(20,40,60,.09);border:1px solid #eef0f2}
.search-bar .placeholder{position:absolute;left:32px;top:24px;font-size:15.5px;color:#9aa1a9}
.btn-search{position:absolute;right:7px;top:7px;width:140px;height:54px;border-radius:27px;background:var(--green);color:#fff;font-size:15px;font-weight:600;display:flex;align-items:center;justify-content:center;gap:8px;letter-spacing:.3px}

.filters{left:297px;top:605px;display:flex;align-items:center;gap:10px}
.filters .label{font-size:13px;font-weight:500;color:var(--ink);margin-right:10px}
.chip{width:171px;height:46px;border-radius:23px;background:var(--chip);font-size:13.5px;font-weight:500;color:var(--ink);display:flex;align-items:center;justify-content:center}

.results-label{left:87px;top:685px;font-size:13.5px;font-weight:500;color:var(--ink)}

/* grid */
.product-grid{left:88px;top:713px;width:1024px;display:grid;grid-template-columns:repeat(5,198px);grid-auto-rows:163px;column-gap:8.5px;row-gap:8px}
.card{background:#fff;border-radius:6px;box-shadow:0 4px 18px rgba(20,40,60,.07);position:relative;text-align:center}
.card h3{margin-top:22px;font-size:16.5px;font-weight:500;color:var(--ink)}
.card .desc{font-size:12.5px;color:var(--muted);margin-top:1px}
.stars{display:flex;justify-content:center;gap:4px;margin-top:9px}
.stars svg{width:17px;height:17px;fill:var(--star)}
.card .rule{position:absolute;left:22px;right:22px;top:112px;height:1px;background:var(--line)}
.card .price{position:absolute;left:21px;top:122px;font-size:21px;font-weight:600;color:var(--green)}
.card .cart{position:absolute;right:22px;top:128px;width:20px;height:20px}

/* pagination */
.pager{left:444px;top:1459px;display:flex;align-items:center;gap:16px;font-size:12px;color:var(--ink)}
.pg-prev{width:76px;height:28px;border-radius:14px;background:var(--chip);display:flex;align-items:center;justify-content:center;gap:5px}
.pg-current{width:30px;height:30px;border-radius:50%;background:var(--orange);color:#fff;display:flex;align-items:center;justify-content:center}
.pg-next{width:76px;height:28px;border-radius:14px;background:var(--ink);color:#fff;font-weight:600;display:flex;align-items:center;justify-content:center;gap:5px}

/* vegetable band */
.veg-band{left:0;top:1560px;width:1200px;height:155px;background:linear-gradient(90deg,#d9382a 0%,#ee8a2e 18%,#5e9a2f 35%,#e7c56d 50%,#8bbd2a 65%,#a8d23a 80%,#6fa23b 100%);border-radius:40% 40% 0 0/40% 40% 0 0}

/* footer */
.footer{left:0;top:1715px;width:1200px;height:530px;background:var(--footer)}
.newsletter-title{left:0;top:1762px;width:1200px;text-align:center;font-size:42px;font-weight:700;color:var(--ink)}
.newsletter-bar{left:276px;top:1824px;width:648px;height:54px;border-radius:27px;background:#fff;box-shadow:0 4px 14px rgba(20,40,60,.06)}
.newsletter-bar .placeholder{position:absolute;left:52px;top:15px;font-size:16px;color:var(--muted)}
.newsletter-bar .mail{position:absolute;left:24px;top:20px}
.btn-subscribe{position:absolute;right:4px;top:3px;width:162px;height:48px;border-radius:24px;background:var(--green);color:#fff;font-size:15px;font-weight:600;display:flex;align-items:center;justify-content:center;letter-spacing:.3px}

.footer-brand{left:87px;top:1977px;font-size:36px;font-weight:700;color:var(--ink);letter-spacing:.5px}
.socials{left:117px;top:2033px;display:flex;gap:6px}
.socials span{width:34px;height:34px;border-radius:50%}
.s1{background:#3b5598}.s2{background:#1da1f2}.s3{background:#dd4b39}.s4{background:#c13584}

.col-divider{top:1925px;width:1px;height:160px;background:#dfe3e8}
.footer-col h4{font-size:18.5px;font-weight:500;color:var(--ink);margin-bottom:18px}
.footer-col li{list-style:none;font-size:14.5px;color:var(--muted);line-height:26.5px}
.contact{left:883px;top:1920px}
.contact h4{font-size:18.5px;font-weight:500;color:var(--ink);margin-bottom:14px}
.contact-item{position:relative;padding-left:22px;margin-bottom:14px}
.contact-item svg{position:absolute;left:0;top:2px;width:14px;height:14px;fill:var(--orange)}
.contact-item b{display:block;font-size:13.5px;font-weight:600;color:var(--ink);line-height:17px}
.contact-item span{display:block;font-size:15px;color:var(--muted);line-height:19px}

.footer-rule{left:87px;top:2185px;width:1024px;height:1px;background:#dfe3e8}
.copyright{left:0;top:2204px;width:1200px;text-align:center;font-size:14px;color:var(--ink)}
.to-top{left:1129px;top:2165px;width:40px;height:40px;border-radius:50%;background:var(--orange);display:flex;align-items:center;justify-content:center}
</style>
</head>
<body>
<svg width="0" height="0" style="position:absolute">
  <defs>
    <symbol id="star" viewBox="0 0 24 24"><path d="M12 1.8l3.1 6.5 7.1.9-5.2 4.9 1.3 7-6.3-3.4-6.3 3.4 1.3-7L1.8 9.2l7.1-.9z"/></symbol>
    <symbol id="cart" viewBox="0 0 24 24"><path d="M2 3h3l2.6 11h11l2.2-8H7" fill="none" stroke="#1c2839" stroke-width="1.8" stroke-linejoin="round" stroke-linecap="round"/><path d="M10 8.5v3M14 8.5v3" stroke="#1c2839" stroke-width="1.6" stroke-linecap="round"/><circle cx="9" cy="19.5" r="1.6" fill="#1c2839"/><circle cx="17" cy="19.5" r="1.6" fill="#1c2839"/></symbol>
  </defs>
</svg>

<header class="abs site-header">
  <div class="abs brand">Tolvane</div>
  <nav class="abs main-nav"><a>HOME</a><a>CURRENT OFFER</a><a>SETTINGS</a></nav>
  <a class="abs btn-login"><svg width="12" height="12" viewBox="0 0 12 12" fill="#fff"><circle cx="6" cy="3.2" r="2.7"/><path d="M.8 12c0-3 2.3-5 5.2-5s5.2 2 5.2 5z"/></svg>LOGIN</a>
  <a class="abs link-logout">LOGOUT</a>
</header>

<section class="abs hero">
  <div class="abs hero-leaf" role="img" aria-label="Tropical leaf in the corner"></div>
  <div class="abs hero-basket" role="img" aria-label="Wicker basket full of vegetables and fruit"></div>
  <h1>Product Search</h1>
  <div class="crumbs">HOME |&nbsp; PRODUCT</div>
</section>

<div class="abs search-bar">
  <span class="placeholder">Search product here...</span>
  <a class="btn-search">SEARCH <svg width="17" height="17" viewBox="0 0 24 24" fill="none" stroke="#fff" stroke-width="2.6" stroke-linecap="round"><circle cx="10.5" cy="10.5" r="7"/><path d="M16 16l5 5"/></svg></a>
</div>

<div class="abs filters">
  <span class="label">FILTERS:</span>
  <span class="chip">PRODUCT GROUP</span>
  <span class="chip">REGION</span>
  <span class="chip">DELIVERY METHOD</span>
</div>

<div class="abs results-label">SEARCH RESULT FARM:</div>

<main class="abs product-grid">
  <article class="card"><h3>Product name</h3><p class="desc">Onions, 3e/kg Tomatoe, e/kg</p><div class="stars"><svg><use href="#star"/></svg><svg><use href="#star"/></svg><svg><use href="#star"/></svg><svg><use href="#star"/></svg><svg><use href="#star"/></svg></div><div class="rule"></div><div class="price">$12.00</div><svg class="cart"><use href="#cart"/></svg></article>
  <article class="card"><h3>Product name</h3><p class="desc">Onions, 3e/kg Tomatoe, e/kg</p><div class="stars"><svg><use href="#star"/></svg><svg><use href="#star"/></svg><svg><use href="#star"/></svg><svg><use href="#star"/></svg><svg><use href="#star"/></svg></div><div class="rule"></div><div class="price">$12.00</div><svg class="cart"><use href="#cart"/></svg></article>
  <article class="card"><h3>Product name</h3><p class="desc">Onions, 3e/kg Tomatoe, e/kg</p><div class="stars"><svg><use href="#star"/></svg><svg><use href="#star"/></svg><svg><use href="#star"/></svg><svg><use href="#star"/></svg><svg><use href="#star"/></svg></div><div class="rule"></div><div class="price">$12.00</div><svg class="cart"><use href="#cart"/></svg></article>
  <article class="card"><h3>Product name</h3><p class="desc">Onions, 3e/kg Tomatoe, e/kg</p><div class="stars"><svg><use href="#star"/></svg><svg><use href="#star"/></svg><svg><use href="#star"/></svg><svg><use href="#star"/></svg><svg><use href="#star"/></svg></div><div class="rule"></div><div class="price">$12.00</div><svg class="cart"><use href="#cart"/></svg></article>
  <article class="card"><h3>Product name</h3><p class="desc">Onions, 3e/kg Tomatoe, e/kg</p><div class="stars"><svg><use href="#star"/></svg><svg><use href="#star"/></svg><svg><use href="#star"/></svg><svg><use href="#star"/></svg><svg><use href="#star"/></svg></div><div class="rule"></div><div class="price">$12.00</div><svg class="cart"><use href="#cart"/></svg></article>

  <article class="card"><h3>Product name</h3><p class="desc">Onions, 3e/kg Tomatoe, e/kg</p><div class="stars"><svg><use href="#star"/></svg><svg><use href="#star"/></svg><svg><use href="#star"/></svg><svg><use href="#star"/></svg><svg><use href="#star"/></svg></div><div class="rule"></div><div class="price">$12.00</div><svg class="cart"><use href="#cart"/></svg></article>
  <article class="card"><h3>Product name</h3><p class="desc">Onions, 3e/kg Tomatoe, e/kg</p><div class="stars"><svg><use href="#star"/></svg><svg><use href="#star"/></svg><svg><use href="#star"/></svg><svg><use href="#star"/></svg><svg><use href="#star"/></svg></div><div class="rule"></div><div class="price">$12.00</div><svg class="cart"><use href="#cart"/></svg></article>
  <article class="card"><h3>Product name</h3><p class="desc">Onions, 3e/kg Tomatoe, e/kg</p><div class="stars"><svg><use href="#star"/></svg><svg><use href="#star"/></svg><svg><use href="#star"/></svg><svg><use href="#star"/></svg><svg><use href="#star"/></svg></div><div class="rule"></div><div class="price">$12.00</div><svg class="cart"><use href="#cart"/></svg></article>
  <article class="card"><h3>Product name</h3><p class="desc">Onions, 3e/kg Tomatoe, e/kg</p><div class="stars"><svg><use href="#star"/></svg><svg><use href="#star"/></svg><svg><use href="#star"/></svg><svg><use href="#star"/></svg><svg><use href="#star"/></svg></div><div class="rule"></div><div class="price">$12.00</div><svg class="cart"><use href="#cart"/></svg></article>
  <article class="card"><h3>Product name</h3><p class="desc">Onions, 3e/kg Tomatoe, e/kg</p><div class="stars"><svg><use href="#star"/></svg><svg><use href="#star"/></svg><svg><use href="#star"/></svg><svg><use href="#star"/></svg><svg><use href="#star"/></svg></div><div class="rule"></div><div class="price">$12.00</div><svg class="cart"><use href="#cart"/></svg></article>

  <article class="card"><h3>Product name</h3><p class="desc">Onions, 3e/kg Tomatoe, e/kg</p><div class="stars"><svg><use href="#star"/></svg><svg><use href="#star"/></svg><svg><use href="#star"/></svg><svg><use href="#star"/></svg><svg><use href="#star"/></svg></div><div class="rule"></div><div class="price">$12.00</div><svg class="cart"><use href="#cart"/></svg></article>
  <article class="card"><h3>Product name</h3><p class="desc">Onions, 3e/kg Tomatoe, e/kg</p><div class="stars"><svg><use href="#star"/></svg><svg><use href="#star"/></svg><svg><use href="#star"/></svg><svg><use href="#star"/></svg><svg><use href="#star"/></svg></div><div class="rule"></div><div class="price">$12.00</div><svg class="cart"><use href="#cart"/></svg></article>
  <article class="card"><h3>Product name</h3><p class="desc">Onions, 3e/kg Tomatoe, e/kg</p><div class="stars"><svg><use href="#star"/></svg><svg><use href="#star"/></svg><svg><use href="#star"/></svg><svg><use href="#star"/></svg><svg><use href="#star"/></svg></div><div class="rule"></div><div class="price">$12.00</div><svg class="cart"><use href="#cart"/></svg></article>
  <article class="card"><h3>Product name</h3><p class="desc">Onions, 3e/kg Tomatoe, e/kg</p><div class="stars"><svg><use href="#star"/></svg><svg><use href="#star"/></svg><svg><use href="#star"/></svg><svg><use href="#star"/></svg><svg><use href="#star"/></svg></div><div class="rule"></div><div class="price">$12.00</div><svg class="cart"><use href="#cart"/></svg></article>
  <article class="card"><h3>Product name</h3><p class="desc">Onions, 3e/kg Tomatoe, e/kg</p><div class="stars"><svg><use href="#star"/></svg><svg><use href="#star"/></svg><svg><use href="#star"/></svg><svg><use href="#star"/></svg><svg><use href="#star"/></svg></div><div class="rule"></div><div class="price">$12.00</div><svg class="cart"><use href="#cart"/></svg></article>

  <article class="card"><h3>Product name</h3><p class="desc">Onions, 3e/kg Tomatoe, e/kg</p><div class="stars"><svg><use href="#star"/></svg><svg><use href="#star"/></svg><svg><use href="#star"/></svg><svg><use href="#star"/></svg><svg><use href="#star"/></svg></div><div class="rule"></div><div class="price">$12.00</div><svg class="cart"><use href="#cart"/></svg></article>
  <article class="card"><h3>Product name</h3><p class="desc">Onions, 3e/kg Tomatoe, e/kg</p><div class="stars"><svg><use href="#star"/></svg><svg><use href="#star"/></svg><svg><use href="#star"/></svg><svg><use href="#star"/></svg><svg><use href="#star"/></svg></div><div class="rule"></div><div class="price">$12.00</div><svg class="cart"><use href="#cart"/></svg></article>
  <article class="card"><h3>Product name</h3><p class="desc">Onions, 3e/kg Tomatoe, e/kg</p><div class="stars"><svg><use href="#star"/></svg><svg><use href="#star"/></svg><svg><use href="#star"/></svg><svg><use href="#star"/></svg><svg><use href="#star"/></svg></div><div class="rule"></div><div class="price">$12.00</div><svg class="cart"><use href="#cart"/></svg></article>
  <article class="card"><h3>Product name</h3><p class="desc">Onions, 3e/kg Tomatoe, e/kg</p><div class="stars"><svg><use href="#star"/></svg><svg><use href="#star"/></svg><svg><use href="#star"/></svg><svg><use href="#star"/></svg><svg><use href="#star"/></svg></div><div class="rule"></div><div class="price">$12.00</div><svg class="cart"><use href="#cart"/></svg></article>
  <article class="card"><h3>Product name</h3><p class="desc">Onions, 3e/kg Tomatoe, e/kg</p><div class="stars"><svg><use href="#star"/></svg><svg><use href="#star"/></svg><svg><use href="#star"/></svg><svg><use href="#star"/></svg><svg><use href="#star"/></svg></div><div class="rule"></div><div class="price">$12.00</div><svg class="cart"><use href="#cart"/></svg></article>
</main>

<nav class="abs pager">
  <span class="pg-prev"><svg width="8" height="8" viewBox="0 0 8 8"><path d="M5.5 1L2.5 4l3 3" fill="none" stroke="#1c2839" stroke-width="1.3"/></svg>Prev</span>
  <span>1</span>
  <span class="pg-current">2</span>
  <span>3</span>
  <span>...</span>
  <span>82</span>
  <span class="pg-next">Next<svg width="8" height="8" viewBox="0 0 8 8"><path d="M2.5 1l3 3-3 3" fill="none" stroke="#fff" stroke-width="1.3"/></svg></span>
</nav>

<div class="abs veg-band" role="img" aria-label="Row of fresh vegetables: tomatoes, carrots, cabbage, cucumbers, potatoes and romanesco"></div>

<footer class="abs footer"></footer>
<h2 class="abs newsletter-title">Newsletter</h2>
<div class="abs newsletter-bar">
  <svg class="mail" width="18" height="13" viewBox="0 0 18 13"><rect width="18" height="13" rx="1.5" fill="#b9c0c8"/><path d="M1 1l8 6 8-6" fill="none" stroke="#fff" stroke-width="1.4"/></svg>
  <span class="placeholder">Enter your email address</span>
  <a class="btn-subscribe">SUBSCRIBE</a>
</div>

<div class="abs footer-brand">Tolvane</div>
<div class="abs socials"><span class="s1"></span><span class="s2"></span><span class="s3"></span><span class="s4"></span></div>

<div class="abs col-divider" style="left:346px"></div>
<div class="abs col-divider" style="left:561px"></div>
<div class="abs col-divider" style="left:822px"></div>

<div class="abs footer-col" style="left:397px;top:1915px">
  <h4>Quick Links</h4>
  <ul><li>Home</li><li>Current Offer</li><li>Settings</li><li>Login/Logout</li></ul>
</div>
<div class="abs footer-col" style="left:627px;top:1917px">
  <h4>Information</h4>
  <ul><li>Terms of use</li><li>Terms and Conditions</li><li>Privacy Policy</li><li>About Us</li><li>FAQ</li></ul>
</div>
<div class="abs contact">
  <h4>Contact Info</h4>
  <div class="contact-item"><svg viewBox="0 0 24 24"><path d="M6.6 10.8a15 15 0 006.6 6.6l2.2-2.2c.3-.3.7-.4 1-.2 1.1.4 2.3.6 3.6.6.6 0 1 .4 1 1V20c0 .6-.4 1-1 1A17 17 0 013 4c0-.6.4-1 1-1h3.5c.6 0 1 .4 1 1 0 1.3.2 2.5.6 3.6.1.3 0 .7-.2 1z"/></svg><b>Phone</b><span>+08 555 014 2290</span></div>
  <div class="contact-item"><svg viewBox="0 0 24 24"><path d="M2 5h20v14H2z"/><path d="M2 5l10 8 10-8" fill="none" stroke="#fff" stroke-width="2"/></svg><b>Email</b><span>hello@tolvane-market.test</span></div>
  <div class="contact-item"><svg viewBox="0 0 24 24"><path d="M12 2a7 7 0 00-7 7c0 5 7 13 7 13s7-8 7-13a7 7 0 00-7-7zm0 9.5A2.5 2.5 0 1112 6.5a2.5 2.5 0 010 5z"/></svg><b>Location</b><span>Some address line goes here<br>city name country</span></div>
</div>

<div class="abs footer-rule"></div>
<div class="abs copyright">© 2020 Copyright - Verdaleaf All Rights Reserved</div>
<a class="abs to-top"><svg width="10" height="10" viewBox="0 0 10 10"><path d="M2 6.5l3-3 3 3" fill="none" stroke="#fff" stroke-width="1.5"/></svg></a>
</body>
</html>
```